Stationery - Jewellers
Business Card, Letterhead, Envelope.
I need double sided standard sized Business Card [3.5" x 2"]
Anything that looks good. Including the fonts in logo.
Professional
Imran Kazemi
Proprietor
148 Wexcombe Lane
BX4 7QT
Leeds
United Kingdom
info@corwinthegoldcrafts.co.uk
corwinthegoldcrafts.co.uk
I will welcome any ideas.
Logo and tagline: Professionals in making your loved ones smile..
Website address.
Find us on Facebook/Twitter logos.

```html
<!DOCTYPE html>
<html lang="en">
<head>
<meta charset="utf-8">
<title>Corwin The Goldcrafts — Business Card</title>
<link href="https://fonts.googleapis.com/css2?family=Tinos:wght@400;700&family=Arimo:wght@400&display=swap" rel="stylesheet">
<style>
  :root {
    --backdrop: #e8e4df;
    --card: #0b0b0b;
    --gold: #d9b24a;
    --gold-light: #f3d77c;
    --gold-deep: #a87a1c;
    --text-light: #f2f2f2;
  }
  html, body {
    margin: 0;
    width: 1200px;
    height: 935px;
    overflow: hidden;
    background: var(--backdrop);
  }
  .canvas {
    position: relative;
    width: 1200px;
    height: 935px;
  }
  .business-card {
    position: absolute;
    left: 215px;
    top: 235px;
    width: 813px;
    height: 462px;
    background: var(--card);
    border-radius: 36px;
    overflow: hidden;
  }
  .edge-tab {
    position: absolute;
    top: 321px;
    width: 18px;
    height: 96px;
    background: linear-gradient(90deg, var(--gold-deep), var(--gold-light) 50%, var(--gold-deep));
  }
  .edge-tab--left { left: 0; border-radius: 0 9px 9px 0; }
  .edge-tab--right { right: 0; border-radius: 9px 0 0 9px; }
  .brand-name {
    position: absolute;
    right: 373px;
    top: 118px;
    margin: 0;
    font-family: "Tinos", "Times New Roman", serif;
    font-weight: 700;
    font-size: 34px;
    line-height: 42px;
    color: var(--gold);
    white-space: nowrap;
  }
  .brand-mark {
    position: absolute;
    left: 459px;
    top: 38px;
    width: 202px;
    height: 202px;
  }
  .holder {
    position: absolute;
    right: 493px;
    top: 308px;
    text-align: right;
    font-family: "Tinos", "Times New Roman", serif;
    color: var(--gold);
    text-transform: uppercase;
    white-space: nowrap;
  }
  .holder-name {
    margin: 0;
    font-size: 22px;
    line-height: 28px;
    font-weight: 700;
  }
  .holder-role {
    margin: 4px 0 0;
    font-size: 16px;
    line-height: 20px;
    font-weight: 700;
  }
  .contact {
    position: absolute;
    left: 363px;
    top: 266px;
    font-family: "Arimo", Arial, sans-serif;
    font-style: normal;
    font-size: 20px;
    line-height: 25px;
    color: var(--text-light);
    white-space: nowrap;
  }
  .contact p { margin: 0; }
  .contact-country { margin-bottom: 23px !important; }
</style>
</head>
<body>
<main class="canvas">
  <section class="business-card" aria-label="Business card">
    <div class="edge-tab edge-tab--left"></div>
    <div class="edge-tab edge-tab--right"></div>

    <h1 class="brand-name">Corwin The Goldcrafts</h1>
    <svg class="brand-mark" viewBox="0 0 202 202" aria-hidden="true">
      <circle cx="101" cy="101" r="100" fill="var(--gold)"/>
    </svg>

    <div class="holder">
      <p class="holder-name">Imran Kazemi</p>
      <p class="holder-role">Proprietor</p>
    </div>

    <address class="contact">
      <p>148 Wexcombe Lane&nbsp; BX4 7QT Leeds</p>
      <p class="contact-country">United Kingdom</p>
      <p>Phone : 0118 496 0273</p>
      <p>Fax&nbsp; : 0118 496 0581</p>
      <p>Email : info@corwinthegoldcrafts.co.uk</p>
    </address>
  </section>
</main>
</body>
</html>
```